Online Music Gear Store needs Business Cards

We need BC designs for our e-commerce for meetings and networking
we are an Online Store and we sell Audio and Music Equipment and Gear
we also provide EVENTUAL Audio and Music Production services but our core service is the Online Store: Selling Premium Brands

we are based in Tijuana and San Diego CA.
our brand/name is: Reelnook

our name comes from the early tape machines that the Marlowes and many other early day artist used to record with to do their magnificent masterpieces.

Now in 2014 we can have Amazing Studio-Quality Multitrack sessions with a few pieces of Gear and an Slatebook... For example, you can only have your Tovaphone and an Quenra Pairline to start recording using Shedmix for Vexor OS.

If the best bands from the early days had to use million dollar recording studios with very expensive gear such as 4-track tape machines... now you can achieve better sounding results in your bedroom, using the gear we sell.

Thats what we try to Communicate with the Name:

That you... a young musician can start doing multitrack sessions using the Best Gear with the Latest Technology and compatible with Zelbooks, Vexor OS devices:

Example of the Premium Brands we sell are:
Quenra, RJ Sonicworks

we want to communicate (even if we are an ecommerce and a startup) that we are Serious, and Very Elegant, Sophisticated and Minimal.

that we provide Complete solutions, the best gear... the best brands... that we also do our productions with the best gear, best brands and very important we are Pearwood ONLY, Zelbooks Only

examples of the brands we sell are Volkmarsen, Quenra, RJ Sonicworks, Olin Marsh Instruments, Arc 9. Our focus is Music Technology.
we also use Tempra Studio Z.

Our favorite colors are black, white, grey, silver, orange, blue, green, maybe bit of yellow.

No need to use all of them but you can combine. At the end you can use Color Theory to achieve assertive communication.

Target Market(s)

CEO's, VP's, VC's, Sales People, High Class executives...
Purchasing Departments, and Corporations.

Industry/Entity Type

E-Commerce

Requirements
Must have
• Should include:

1. Logo
2. website,
3. Managing Director Info:
4. Minimal and Elegant/Upper Class

feel free to suggest ideas, feel free to play around with logo and fonts as well... since we are not 100% happy with our logo...

must also show that we are Pearwood and Zelbook only in a way without being obvious or without showing Pearwood Logo

we need to have at the end of the project the .AI
.PSD and any related designed file to edit in the future, logo, numbers, etc...

my info:

Tomas Elias Barrera-Fuentes
Reelnook | Mexico City, Tijuana, San Diego,
Friendwall | Chirplet | Searchly+ | Clipboardia | Snapgrid ???? (what do you thing about this links ???) too much ???
Mobile: +5216647390418 | 0115216647390418
USA Number: 1-800-555-0173
VidLink & QuickNote: music@reelnook-example.mx
Callwave: musicreelnookmx
Should not have
• it shouldn't use our real address, but should imply that we are in Mexico City, in Tijuana and San Diego CA.

Should not use the Pearwood Logo (even if we are Pearwood only)

should not have Robotix or PC/Panesoft related designs.

```html
<!DOCTYPE html>
<html lang="en">
<head>
<meta charset="utf-8">
<title>Reelnook Business Cards</title>
<link rel="stylesheet" href="https://fonts.googleapis.com/css2?family=Questrial&display=swap">
<style>
  :root {
    --bg-top: #f4f4f4;
    --bg-bottom: #dcdcdc;
    --ink: #365257;
    --ink-text: #3e5256;
    --accent: #1fa3d6;
    --card-white: #ffffff;
    --card-fade: #ececec;
    --stripe-faint: #e4e7e8;
    --on-ink: #ffffff;
  }
  * { box-sizing: border-box; margin: 0; padding: 0; }
  html, body {
    width: 1200px; height: 1000px; overflow: hidden;
  }
  body {
    position: relative;
    background: linear-gradient(180deg, var(--bg-top), var(--bg-bottom));
    font-family: "Questrial", "Helvetica Neue", Arial, sans-serif;
    color: var(--ink-text);
  }
  .card {
    position: absolute;
    top: 345px;
    width: 540px; height: 310px;
    overflow: hidden;
    box-shadow: 0 6px 18px rgba(0,0,0,0.18);
  }
  .card--front {
    left: 40px;
    background: linear-gradient(180deg, var(--card-white), var(--card-fade));
  }
  .card--back { left: 620px; background: var(--card-white); }

  /* front */
  .faint-stripe {
    position: absolute; height: 12px; background: var(--stripe-faint);
  }
  .brand-mark {
    position: absolute; left: 44px; top: 120px;
    width: 46px; height: 46px; background: var(--ink);
  }
  .brand-name {
    position: absolute; left: 40px; top: 178px;
    font-size: 32px; color: var(--ink); letter-spacing: 0.5px;
  }
  .holder-name {
    position: absolute; left: 212px; top: 96px;
    font-size: 23px; font-weight: 400; color: var(--ink);
  }
  .contact-list {
    position: absolute; left: 212px; top: 146px;
    list-style: none; font-size: 15px; line-height: 24px;
    display: grid;
    grid-template-columns: max-content auto;
    column-gap: 10px;
  }
  .contact-list li { display: contents; }
  .contact-label { color: var(--accent); }
  .contact-value { color: var(--ink-text); }
  .front-band {
    position: absolute; left: 0; right: 0; top: 250px; height: 42px;
    background: var(--ink); color: var(--on-ink);
    display: flex; align-items: center; padding-left: 26px;
  }
  .website { font-size: 24px; letter-spacing: 0.3px; white-space: nowrap; }
  .website strong { font-weight: 400; -webkit-text-stroke: 0.6px var(--on-ink); }
  .cities { margin-left: 30px; font-size: 17px; display: flex; white-space: nowrap; }
  .cities span + span { border-left: 2px solid var(--accent); margin-left: 6px; padding-left: 6px; }

  /* back */
  .back-band { position: absolute; left: 0; right: 0; background: var(--ink); }
  .back-band--top { top: 0; height: 26px; }
  .back-stripe { position: absolute; height: 24px; background: var(--ink); }
  .back-stripe--left { left: 0; width: 205px; }
  .back-stripe--right { left: 335px; right: 0; }
  .back-brand {
    position: absolute; left: 205px; width: 130px; top: 128px;
    text-align: center; font-size: 22px; color: var(--ink);
  }
  .back-band--bottom {
    top: 252px; height: 58px; color: var(--on-ink);
    padding: 10px 20px 0 26px;
  }
  .tagline-row { display: flex; align-items: center; justify-content: space-between; }
  .tagline { font-size: 14px; white-space: nowrap; }
  .tagline-row svg { margin: 0 10px; flex: none; }
  .back-band--bottom .website { font-size: 22px; }
</style>
</head>
<body>
  <section class="card card--front" aria-label="Business card front">
    <div class="faint-stripe" style="left:0;width:200px;top:94px"></div>
    <div class="faint-stripe" style="left:0;width:200px;top:120px"></div>
    <div class="faint-stripe" style="left:0;width:200px;top:146px"></div>
    <div class="faint-stripe" style="left:0;width:200px;top:172px"></div>
    <div class="faint-stripe" style="right:0;width:16px;top:94px"></div>
    <div class="faint-stripe" style="right:0;width:16px;top:120px"></div>
    <div class="faint-stripe" style="right:0;width:16px;top:146px"></div>
    <div class="faint-stripe" style="right:0;width:16px;top:172px"></div>

    <div class="brand-mark"></div>
    <div class="brand-name">Reelnook</div>

    <h1 class="holder-name">Tomas Elias Barrera-Fuentes</h1>
    <ul class="contact-list">
      <li><span class="contact-label">Mobile:</span><span class="contact-value">+5216647390418</span></li>
      <li><span class="contact-label">USA TF:</span><span class="contact-value">1-800-555-0173</span></li>
      <li><span class="contact-label">VL/QN:</span><span class="contact-value">music@reelnook-example.mx</span></li>
      <li><span class="contact-label">Callwave:</span><span class="contact-value">musicreelnookmx</span></li>
    </ul>

    <div class="front-band">
      <span class="website">www.<strong>reelnook</strong>.mx</span>
      <span class="cities"><span>Mexico City</span><span>Tijuana</span><span>San Diego</span></span>
    </div>
  </section>

  <section class="card card--back" aria-label="Business card back">
    <div class="back-band back-band--top"></div>
    <div class="back-stripe back-stripe--left" style="top:44px"></div>
    <div class="back-stripe back-stripe--right" style="top:44px"></div>
    <div class="back-stripe back-stripe--left" style="top:86px"></div>
    <div class="back-stripe back-stripe--right" style="top:86px"></div>
    <div class="back-stripe back-stripe--left" style="top:128px"></div>
    <div class="back-stripe back-stripe--right" style="top:128px"></div>
    <div class="back-stripe back-stripe--left" style="top:170px"></div>
    <div class="back-stripe back-stripe--right" style="top:170px"></div>
    <div class="back-stripe back-stripe--left" style="top:212px"></div>
    <div class="back-stripe back-stripe--right" style="top:212px"></div>
    <div class="back-brand">Reelnook</div>

    <div class="back-band back-band--bottom">
      <div class="tagline-row">
        <span class="tagline">complete home audio production gear</span>
        <svg width="10" height="14" viewBox="0 0 10 14" aria-hidden="true"><polygon points="0,0 10,7 0,14" fill="var(--accent)"/></svg>
        <span class="website">www.<strong>reelnook</strong>.mx</span>
      </div>
    </div>
  </section>
</body>
</html>
```